New App: 4 Page Design - Updated Brief

We need an indicative design for our new app 'Bolt Haul', a delivery service for tools and hardware in Sydney, Australia.

Imagine a service which copies the blue print of Ferro Meals, but for tools and Hardware. Where builders and tradespeople are stuck on-site at work and need a tool to be delivered to them on-site, same day. They can jump onto this app and in-put their address, then select an item from the catalogue and confirm the order. Once the order has been collected and due for delivery a map will show the location of the delivery driver.

We'd like 4 pages designed.

1st page) Loading page, similar to but not the same as the FerroMeals example attached.

2nd page) Home page - featuring the logo and some icons which direct users around the website. (Please see link to design example: https://www.ferromeals-example.com/au?ref_id=aa11bb22-c333-4d44-85e5-ff66aa77bb88 )

3rd page) A page which depicts the catalogue of tools and hardware (showing generic tools available (Please see link to design example https://www.kelmtrade-example.com.au/products/building-hardware).

4th page) We'd like a page which shows a map, tracking the delivery, from the hardware store, to the location of the purchaser, exactly like any typical ferro delivery service.

Please see the below website for design guidance and ideas

https://www.kelmtrade-example.com.au/?src=xx.yy&tid=Zq4RtL8mNw2PvX6sKd0HfJ3bYc9GuE7aTo1LiVn5MeWx_xyz

Target Market(s)

Construction industry, tradespeople

Industry/Entity Type

Construction and Tradesmen

Colors

Designer to choose colors to be used in the design.

Requirements
Must have
• Desired Colour schemes: up to the designer but no bright colours
Nice to have
• An icon bar at the bottom of the page that directs you to the various pages on the app. Example shown in the attachments
Should not have
• An exact copy of the Ferro App

```html
<!DOCTYPE html>
<html lang="en">
<head>
<meta charset="utf-8">
<title>Bolt Haul – App Screens</title>
<link href="https://fonts.googleapis.com/css2?family=Poppins:wght@400;500;600;700;800&display=swap" rel="stylesheet">
<style>
:root{
  --ink:#161616;
  --ink-soft:#262626;
  --yellow:#f5b400;
  --orange:#f39a1e;
  --paper:#ffffff;
  --mist:#f4f4f4;
  --grey:#8a8a8a;
  --line:#e6e6e6;
  --stage:#f7f5f1;
}
*{box-sizing:border-box;margin:0;padding:0}
html,body{width:1200px;height:864px;overflow:hidden}
body{background:var(--stage);font-family:"Poppins",sans-serif;color:var(--ink);display:flex;align-items:center;justify-content:center;gap:18px}
.icon{width:12px;height:12px;fill:none;stroke:currentColor;stroke-width:2;stroke-linecap:round;stroke-linejoin:round}
.screen{position:relative;width:216px;height:468px;border-radius:28px;overflow:hidden;background:var(--mist);box-shadow:0 0 0 5px var(--ink),0 10px 24px rgba(0,0,0,.18)}
.status{position:absolute;top:0;left:0;right:0;height:28px;display:flex;align-items:center;justify-content:space-between;padding:0 16px;font-size:9px;font-weight:600;z-index:3;color:#fff}
.status.dark-text{color:var(--ink)}
.status .bars{display:flex;gap:3px;align-items:center}
.status .bars i{display:block;width:13px;height:6px;border-radius:2px;background:currentColor}
.status .bars b{display:block;width:5px;height:6px;border-radius:1px;background:currentColor}
.home-bar{position:absolute;bottom:6px;left:50%;width:72px;height:3px;margin-left:-36px;border-radius:2px;background:#fff;z-index:5}
.home-bar.dark{background:var(--ink)}

/* splash */
.splash{background:var(--ink)}
.splash .photo{position:absolute;inset:0;background:linear-gradient(180deg,#2a2a2a 0%,#1c1c1c 45%,#3a2a18 100%)}
.brand{position:absolute;top:190px;left:0;right:0;display:flex;flex-direction:column;align-items:center;gap:12px}
.brand .dot{width:58px;height:58px;border-radius:50%;background:var(--yellow)}
.brand .name{font-size:17px;font-weight:800;color:var(--yellow);letter-spacing:.5px}

/* home */
.hero{position:absolute;top:0;left:0;right:0;height:150px;background:linear-gradient(180deg,#1a1a1a,#2b2b2b)}
.address{position:absolute;top:32px;left:12px;right:12px;display:flex;align-items:center;gap:8px;z-index:2}
.address .mark{width:22px;height:22px;border-radius:50%;background:var(--yellow);flex:none}
.address .label{font-size:5.5px;color:#cfcfcf;letter-spacing:.4px}
.address .value{font-size:8px;font-weight:600;color:var(--yellow);display:flex;align-items:center;gap:3px}
.address .value .icon{width:7px;height:7px}
.cart{margin-left:auto;position:relative;color:#fff}
.cart .icon{width:12px;height:12px}
.cart .badge{position:absolute;top:-6px;right:-6px;width:9px;height:9px;border-radius:50%;background:var(--orange);color:#fff;font-size:5.5px;font-weight:700;display:flex;align-items:center;justify-content:center}
.search{position:absolute;top:68px;left:12px;right:12px;height:24px;border-radius:6px;background:rgba(255,255,255,.08);display:flex;align-items:center;gap:6px;padding:0 9px;color:#e0e0e0;font-size:7px;z-index:2}
.search .icon{width:9px;height:9px}
.yellow-band{position:absolute;top:108px;left:0;right:0;height:10px;background:var(--yellow);z-index:1}
.cat-card{position:absolute;top:100px;left:12px;right:12px;height:86px;border-radius:8px;background:var(--paper);padding:8px 9px;z-index:2;box-shadow:0 2px 6px rgba(0,0,0,.06)}
.head-row{display:flex;justify-content:space-between;align-items:baseline}
.head-row h3{font-size:9px;font-weight:600}
.head-row a{font-size:6.5px;font-weight:600;color:var(--yellow);text-decoration:none}
.cats{display:flex;justify-content:space-between;margin-top:6px}
.cat{width:40px;text-align:center;font-size:5px;line-height:1.35;color:#333}
.cat .thumb{width:28px;height:28px;margin:0 auto 3px;border-radius:50%}
.t-steel{background:linear-gradient(135deg,#9aa3ad,#3d444c)}
.t-concrete{background:linear-gradient(135deg,#c9b8a8,#7b6d62)}
.t-boards{background:linear-gradient(135deg,#e8c49c,#9b5a2c)}
.t-fast{background:linear-gradient(135deg,#a9b4bf,#4f5963)}
.section{position:absolute;left:12px;right:0}
.kicker{font-size:5.5px;color:var(--grey);letter-spacing:.3px}
.section h2{font-size:9.5px;font-weight:600;margin:1px 0 6px}
.stores{display:flex;gap:6px}
.store{position:relative;width:76px;height:90px;flex:none;border-radius:6px;overflow:hidden;color:#fff}
.store .pic{position:absolute;inset:0}
.s-cobalt{background:linear-gradient(160deg,#9b2a1e,#4d1510)}
.s-marlin{background:linear-gradient(180deg,#4ca6d6 0%,#3a9d4a 60%,#30343a)}
.s-tarra{background:linear-gradient(160deg,#d9322b,#7a1a14)}
.store .chip{position:absolute;top:5px;left:5px;background:var(--yellow);color:var(--ink);border-radius:6px;font-size:4.5px;font-weight:700;padding:1px 4px;letter-spacing:.2px}
.store .info{position:absolute;left:6px;bottom:6px;font-size:6px;font-weight:600;line-height:1.3}
.store .info span{display:block;font-weight:400;font-size:5px}
.dots{display:flex;gap:3px;justify-content:center;margin:6px 12px 0 0}
.dots i{width:3px;height:3px;border-radius:50%;background:#bbb}
.dots i:first-child{width:14px;border-radius:2px;background:var(--ink)}
.products{display:flex;gap:8px;padding-right:12px}
.product{flex:1;background:var(--paper);border-radius:6px;padding:6px;font-size:5.5px;line-height:1.35}
.product .pic{height:60px;border-radius:4px;margin-bottom:5px}
.p-box{background:linear-gradient(135deg,#eaeef2,#c7d2dc)}
.p-angle{background:linear-gradient(135deg,#eeeeee,#cfcfcf)}
.product .meta{display:flex;justify-content:space-between;align-items:baseline;margin-top:2px}
.product .price{color:var(--orange);font-weight:600;font-size:6px}
.product .sold{color:var(--grey);font-size:4.5px}
.tabbar{position:absolute;left:0;right:0;bottom:0;height:50px;background:var(--ink);display:flex;justify-content:space-around;padding-top:8px;z-index:4}
.tab{display:flex;flex-direction:column;align-items:center;gap:2px;font-size:5px;color:#9a9a9a}
.tab .icon{width:12px;height:12px}
.tab.active{color:var(--yellow)}
.eta-sheet{position:absolute;left:0;right:0;bottom:50px;height:66px;background:var(--paper);border-radius:12px 12px 0 0;text-align:center;padding-top:6px;z-index:3}
.grip{width:24px;height:2px;border-radius:2px;background:#ddd;margin:0 auto 8px}
.eta-label{font-size:6px;color:#444}
.eta{font-size:11px;font-weight:600;margin-top:1px}
.progress{height:3px;border-radius:2px;background:#f3e9d8;margin:7px 12px 0;overflow:hidden}
.progress i{display:block;height:100%;width:72%;background:var(--orange)}

/* store page */
.banner{position:absolute;top:0;left:0;right:0;height:88px;background:linear-gradient(160deg,#3b3b3b 0%,#7a2217 55%,#a0281b 100%)}
.back{position:absolute;top:30px;left:10px;width:22px;height:22px;border-radius:50%;background:#fff;color:var(--yellow);display:flex;align-items:center;justify-content:center;z-index:3;box-shadow:0 1px 4px rgba(0,0,0,.15)}
.back .icon{width:10px;height:10px}
.store-body{position:absolute;top:88px;left:0;right:0;bottom:0;background:var(--paper)}
.store-head{padding:9px 12px 0}
.store-head h1{font-size:11px;font-weight:600}
.sub-row{display:flex;justify-content:space-between;align-items:center;font-size:6.5px;color:#444;margin-top:1px}
.stars{display:flex;gap:1px;color:var(--yellow)}
.stars svg{width:7px;height:7px;fill:currentColor}
.delivery-row{display:flex;align-items:center;gap:5px;margin-top:9px;font-size:8px;font-weight:500}
.delivery-row .icon{width:11px;height:11px;color:var(--yellow)}
.map-btn{margin-left:auto;background:var(--ink);color:#fff;border-radius:8px;font-size:5.5px;font-weight:500;padding:4px 7px;display:flex;align-items:center;gap:3px}
.map-btn .icon{width:7px;height:7px;color:#fff}
.tabs{display:flex;gap:9px;padding:10px 12px 0;font-size:5.5px;font-weight:500;white-space:nowrap;border-bottom:1px solid var(--line)}
.tabs span{padding-bottom:5px}
.tabs .on{color:var(--yellow);border-bottom:2px solid var(--yellow)}
.catalogue{background:var(--mist);position:absolute;top:116px;left:0;right:0;bottom:0;padding:8px 12px}
.cat-head{display:flex;justify-content:space-between;align-items:flex-start}
.cat-head h2{font-size:9.5px;font-weight:600}
.cat-head p{font-size:5.5px;color:var(--grey)}
.filter{width:20px;height:20px;border-radius:50%;background:#fff;color:var(--yellow);display:flex;align-items:center;justify-content:center}
.filter .icon{width:9px;height:9px}
.grid{display:grid;grid-template-columns:1fr 1fr;gap:8px;margin-top:8px}
.grid .product .pic{height:78px}
.cart-bar{position:absolute;left:10px;right:10px;bottom:20px;height:26px;border-radius:7px;background:var(--ink);color:#fff;display:flex;align-items:center;padding:0 8px;font-size:7.5px;font-weight:500;z-index:4}
.cart-bar .count{width:14px;height:14px;border-radius:50%;background:#fff;color:var(--ink);font-size:5.5px;font-weight:700;display:flex;align-items:center;justify-content:center}
.cart-bar .label{flex:1;text-align:center}
.fade{position:absolute;left:0;right:0;bottom:0;height:60px;background:linear-gradient(180deg,rgba(255,255,255,0),#fff 55%);z-index:3}

/* tracking */
.map{position:absolute;top:0;left:0;right:0;height:210px;background:linear-gradient(160deg,#dfe5e2 0%,#e8ece6 45%,#9fc2e3 100%)}
.track-sheet{position:absolute;top:200px;left:0;right:0;bottom:0;background:var(--paper);border-radius:12px 12px 0 0;padding-top:6px}
.track-sheet .eta-block{text-align:center}
.order{padding:12px 12px 0}
.order h2{font-size:9px;font-weight:600;margin-bottom:6px}
.row{display:flex;justify-content:space-between;align-items:flex-start;font-size:6.5px;color:#555;margin-bottom:10px}
.row b{font-weight:600;color:var(--ink);text-align:right;line-height:1.55}
.row .tag{background:var(--mist);border-radius:6px;padding:2px 5px;font-size:5.5px}
.row .accent{color:var(--orange);font-weight:500}
.row .muted{color:var(--grey)}
.rule{height:1px;background:var(--line);margin:2px 0 10px}
.details{display:flex;justify-content:space-between;align-items:center;font-size:7px;font-weight:600}
.details small{font-weight:400;font-size:5.5px;color:var(--grey)}
.details .chev{width:13px;height:13px;border-radius:3px;background:var(--ink);color:#fff;display:flex;align-items:center;justify-content:center}
.details .chev .icon{width:8px;height:8px}
</style>
</head>
<body>

<svg width="0" height="0" style="position:absolute" aria-hidden="true">
  <symbol id="i-cart" viewBox="0 0 24 24"><path d="M3 4h3l2.5 11h10L21 7H7"/><circle cx="10" cy="20" r="1.5"/><circle cx="17" cy="20" r="1.5"/></symbol>
  <symbol id="i-search" viewBox="0 0 24 24"><circle cx="11" cy="11" r="7"/><path d="M20 20l-4-4"/></symbol>
  <symbol id="i-home" viewBox="0 0 24 24"><path d="M4 11l8-7 8 7v9h-5v-6H9v6H4z"/></symbol>
  <symbol id="i-bell" viewBox="0 0 24 24"><path d="M6 17V11a6 6 0 0 1 12 0v6l2 2H4z"/><path d="M10 21h4"/></symbol>
  <symbol id="i-gear" viewBox="0 0 24 24"><circle cx="12" cy="12" r="3"/><path d="M12 2v3M12 19v3M2 12h3M19 12h3M4.9 4.9l2.1 2.1M17 17l2.1 2.1M4.9 19.1L7 17M17 7l2.1-2.1"/></symbol>
  <symbol id="i-down" viewBox="0 0 24 24"><path d="M6 9l6 6 6-6"/></symbol>
  <symbol id="i-back" viewBox="0 0 24 24"><path d="M19 12H5M11 6l-6 6 6 6"/></symbol>
  <symbol id="i-clock" viewBox="0 0 24 24"><circle cx="12" cy="12" r="9"/><path d="M12 7v5l3 2"/></symbol>
  <symbol id="i-pin" viewBox="0 0 24 24"><path d="M12 22s7-7 7-12a7 7 0 0 0-14 0c0 5 7 12 7 12z"/><circle cx="12" cy="10" r="2.5"/></symbol>
  <symbol id="i-filter" viewBox="0 0 24 24"><path d="M4 7h16M7 12h10M10 17h4"/></symbol>
  <symbol id="i-star" viewBox="0 0 24 24"><path d="M12 2l3 7 7 .6-5.4 4.7 1.7 7.2L12 17.8 5.7 21.5l1.7-7.2L2 9.6 9 9z"/></symbol>
</svg>

<!-- Splash -->
<section class="screen splash" aria-label="Loading screen">
  <div class="photo" role="img" aria-label="Dark construction site with cranes at dusk"></div>
  <div class="status"><span>9:41</span><span class="bars"><i></i><b></b></span></div>
  <div class="brand"><span class="dot"></span><span class="name">BOLT HAUL</span></div>
  <div class="home-bar"></div>
</section>

<!-- Home -->
<section class="screen" aria-label="Home screen">
  <div class="hero" role="img" aria-label="Dark construction site backdrop"></div>
  <div class="status"><span>9:41</span><span class="bars"><i></i><b></b></span></div>
  <div class="address">
    <span class="mark"></span>
    <div><div class="label">DELIVERY ADDRESS</div><div class="value">Enter Your Location <svg class="icon"><use href="#i-down"/></svg></div></div>
    <div class="cart"><svg class="icon"><use href="#i-cart"/></svg><span class="badge">3</span></div>
  </div>
  <div class="search"><svg class="icon"><use href="#i-search"/></svg>Search product or store</div>
  <div class="yellow-band"></div>
  <div class="cat-card">
    <div class="head-row"><h3>Categories</h3><a href="#">SEE ALL</a></div>
    <div class="cats">
      <div class="cat"><div class="thumb t-steel" role="img" aria-label="Steel beams"></div>Steel &amp;<br>Aluminum</div>
      <div class="cat"><div class="thumb t-concrete" role="img" aria-label="Concrete pour"></div>Concrete &amp;<br>Cementing</div>
      <div class="cat"><div class="thumb t-boards" role="img" aria-label="Stacked timber boards"></div>Building<br>Boards</div>
      <div class="cat"><div class="thumb t-fast" role="img" aria-label="Screws and fixings"></div>Fasteners &amp;<br>Fixings</div>
    </div>
  </div>
  <div class="section" style="top:196px">
    <div class="kicker">DAILY DISCOVER</div>
    <h2>Featured Hardware Stores</h2>
    <div class="stores">
      <div class="store"><div class="pic s-cobalt" role="img" aria-label="Hardware store front"></div><span class="chip">FEATURED</span><div class="info">Cobalt Hardware<span>1.5 km</span></div></div>
      <div class="store"><div class="pic s-marlin" role="img" aria-label="Hardware depot exterior"></div><span class="chip">FEATURED</span><div class="info">Marlin Depot<span>2 km</span></div></div>
      <div class="store"><div class="pic s-tarra" role="img" aria-label="Hardware store signage"></div><span class="chip">FEATURED</span><div class="info">Tarra Hard<span>2.3 km</span></div></div>
    </div>
    <div class="dots"><i></i><i></i><i></i><i></i></div>
  </div>
  <div class="section" style="top:340px">
    <div class="kicker">DAILY DISCOVER</div>
    <h2>Popular Products</h2>
    <div class="products">
      <div class="product"><div class="pic p-box" role="img" aria-label="Blue steel box section"></div>Site Ready Supplies<br>50 x 50 x 2.0m…</div>
      <div class="product"><div class="pic p-angle" role="img" aria-label="Steel angle bar"></div>Site Ready Supplies<br>50 x 50 x 2.0m…</div>
    </div>
  </div>
  <nav class="tabbar">
    <span class="tab active"><svg class="icon"><use href="#i-home"/></svg>Home</span>
    <span class="tab"><svg class="icon"><use href="#i-search"/></svg>Browse</span>
    <span class="tab"><svg class="icon"><use href="#i-bell"/></svg>Notifications</span>
    <span class="tab"><svg class="icon"><use href="#i-gear"/></svg>Settings</span>
  </nav>
  <div class="home-bar"></div>
</section>

<!-- Home with delivery in progress -->
<section class="screen" aria-label="Home screen with active delivery">
  <div class="hero" role="img" aria-label="Dark construction site backdrop"></div>
  <div class="status"><span>9:41</span><span class="bars"><i></i><b></b></span></div>
  <div class="address">
    <span class="mark"></span>
    <div><div class="label">DELIVERY ADDRESS</div><div class="value">Enter Your Location <svg class="icon"><use href="#i-down"/></svg></div></div>
    <div class="cart"><svg class="icon"><use href="#i-cart"/></svg><span class="badge">3</span></div>
  </div>
  <div class="search"><svg class="icon"><use href="#i-search"/></svg>Search product or store</div>
  <div class="yellow-band"></div>
  <div class="cat-card">
    <div class="head-row"><h3>Categories</h3><a href="#">SEE ALL</a></div>
    <div class="cats">
      <div class="cat"><div class="thumb t-steel" role="img" aria-label="Steel beams"></div>Steel &amp;<br>Aluminum</div>
      <div class="cat"><div class="thumb t-concrete" role="img" aria-label="Concrete pour"></div>Concrete &amp;<br>Cementing</div>
      <div class="cat"><div class="thumb t-boards" role="img" aria-label="Stacked timber boards"></div>Building<br>Boards</div>
      <div class="cat"><div class="thumb t-fast" role="img" aria-label="Screws and fixings"></div>Fasteners &amp;<br>Fixings</div>
    </div>
  </div>
  <div class="section" style="top:196px">
    <div class="kicker">DAILY DISCOVER</div>
    <h2>Featured Hardware Stores</h2>
    <div class="stores">
      <div class="store"><div class="pic s-cobalt" role="img" aria-label="Hardware store front"></div><span class="chip">FEATURED</span><div class="info">Cobalt Hardware<span>1.5 km</span></div></div>
      <div class="store"><div class="pic s-marlin" role="img" aria-label="Hardware depot exterior"></div><span class="chip">FEATURED</span><div class="info">Marlin Depot<span>2 km</span></div></div>
      <div class="store"><div class="pic s-tarra" role="img" aria-label="Hardware store signage"></div><span class="chip">FEATURED</span><div class="info">Tarra Hard<span>2.3 km</span></div></div>
    </div>
    <div class="dots"><i></i><i></i><i></i><i></i></div>
  </div>
  <div class="eta-sheet">
    <div class="grip"></div>
    <div class="eta-label">Estimated delivery time</div>
    <div class="eta">5 - 10 mins</div>
    <div class="progress"><i></i></div>
  </div>
  <nav class="tabbar">
    <span class="tab active"><svg class="icon"><use href="#i-home"/></svg>Home</span>
    <span class="tab"><svg class="icon"><use href="#i-search"/></svg>Browse</span>
    <span class="tab"><svg class="icon"><use href="#i-bell"/></svg>Notifications</span>
    <span class="tab"><svg class="icon"><use href="#i-gear"/></svg>Settings</span>
  </nav>
  <div class="home-bar"></div>
</section>

<!-- Store catalogue -->
<section class="screen" aria-label="Store catalogue">
  <div class="banner" role="img" aria-label="Hardware store shopfront with red signage"></div>
  <div class="status"><span>9:41</span><span class="bars"><i></i><b></b></span></div>
  <div class="back"><svg class="icon"><use href="#i-back"/></svg></div>
  <div class="store-body">
    <div class="store-head">
      <h1>Cobalt Hardware</h1>
      <div class="sub-row"><span>0.7 km away</span>
        <span class="stars"><svg><use href="#i-star"/></svg><svg><use href="#i-star"/></svg><svg><use href="#i-star"/></svg><svg><use href="#i-star"/></svg><svg><use href="#i-star"/></svg></span></div>
      <div class="delivery-row"><svg class="icon"><use href="#i-clock"/></svg>Delivery 20 min
        <span class="map-btn"><svg class="icon"><use href="#i-pin"/></svg>View Map</span></div>
    </div>
    <div class="tabs"><span class="on">Popular</span><span>Steel &amp; Aluminum</span><span>Roofing</span><span>Building Boards</span><span>Fas</span></div>
    <div class="catalogue">
      <div class="cat-head">
        <div><h2>Popular Products</h2><p>Most ordered this week.</p></div>
        <span class="filter"><svg class="icon"><use href="#i-filter"/></svg></span>
      </div>
      <div class="grid">
        <div class="product"><div class="pic p-box" role="img" aria-label="Blue steel box section"></div>Site Ready Supplies<br>50 x 50 x 2.0m…<div class="meta"><span class="price">$65.30</span><span class="sold">5.2K Sold</span></div></div>
        <div class="product"><div class="pic p-angle" role="img" aria-label="Steel angle bar"></div>Site Ready Supplies<br>50 x 50 x 2.0m…<div class="meta"><span class="price">$65.30</span><span class="sold">10.4K Sold</span></div></div>
        <div class="product"><div class="pic p-box" role="img" aria-label="Blue steel box section"></div></div>
        <div class="product"><div class="pic p-angle" role="img" aria-label="Steel angle bar"></div></div>
      </div>
    </div>
  </div>
  <div class="fade"></div>
  <div class="cart-bar"><span class="count">12</span><span class="label">View Your Cart</span><span>$1,080.50</span></div>
  <div class="home-bar dark"></div>
</section>

<!-- Tracking -->
<section class="screen" aria-label="Delivery tracking">
  <div class="map" role="img" aria-label="Street map showing store, driver and delivery pins"></div>
  <div class="status dark-text"><span>9:41</span><span class="bars"><i></i><b></b></span></div>
  <div class="back"><svg class="icon"><use href="#i-back"/></svg></div>
  <div class="track-sheet">
    <div class="eta-block">
      <div class="grip"></div>
      <div class="eta-label">Estimated delivery time</div>
      <div class="eta">5 - 10 mins</div>
      <div class="progress"><i></i></div>
    </div>
    <div class="order">
      <h2>Order Details</h2>
      <div class="row"><span>Order Number</span><b class="tag">#DP09-QHA84</b></div>
      <div class="row"><span>Order From</span><span class="accent">Cobalt Hardware - Uptown</span></div>
      <div class="row"><span>Delivery Address</span><b>Mrs Hale 42 Wattle Street<br>BRAVEN QLD 4000 AUSTRALIA</b></div>
      <div class="row"><span>Total <span class="muted">(inc. VAT)</span></span><b>$1,080.50</b></div>
      <div class="rule"></div>
      <div class="details"><span>View Details <small>(12 items)</small></span><span class="chev"><svg class="icon"><use href="#i-down"/></svg></span></div>
    </div>
  </div>
  <div class="home-bar dark"></div>
</section>

</body>
</html>
```